Industrial/Commercial Plumbing Capability Statement

Would like a construction capability statement/Brochure amended to be similar to the attached. -
Have included photos and Notes on the attached
would like project photos to be used
This is a previous capability statement that we would like amended and altered to include, safety, QA and Recent Projects
Please use our company logo
Updates

Need extra days to review

Target Market(s)

Construction work - Industrial

Industry/Entity Type

Plumbing

Requirements
Must have
• Include all items in contents page

Eye Catching Photos relevant to construction industry and relevant to topic on page

```html
<!DOCTYPE html>
<html lang="en">
<head>
<meta charset="utf-8">
<title>Harbourline Plumbing – Capability Statement Spread</title>
<link rel="stylesheet" href="https://fonts.googleapis.com/css2?family=Barlow:ital,wght@0,300;0,400;0,600;0,700;1,300;1,400&display=swap">
<style>
  :root{
    --bg:#e6e6e6;
    --ink-dark:#0f0f0c;
    --olive:#6f7a1e;
    --lime:#c8d23a;
    --teal:#1f5c73;
    --blue-deep:#163f5a;
    --blue:#1f5475;
    --blue-light:#3d7393;
    --white:#ffffff;
    --soft:#dfe8ee;
    --photo:#9a9a9a;
  }
  *{box-sizing:border-box;margin:0;padding:0}
  html,body{width:1200px;height:857px;overflow:hidden;background:var(--bg)}
  body{font-family:"Barlow",sans-serif;color:var(--white)}
  .spread{position:absolute;left:50px;top:40px;width:1100px;height:778px;display:flex;box-shadow:0 6px 20px rgba(0,0,0,.18)}
  .page{position:relative;width:550px;height:778px;overflow:hidden}

  /* Left page */
  .page--feature{background:var(--ink-dark)}
  .feature-image{position:absolute;inset:0;background:
      radial-gradient(ellipse 60% 45% at 70% 55%,rgba(200,210,58,.55),transparent 70%),
      radial-gradient(ellipse 45% 40% at 32% 36%,rgba(170,180,40,.45),transparent 70%),
      linear-gradient(160deg,#0c0c09 0%,#3a4010 45%,#1a1c0c 75%,#0c0c09 100%)}
  .section-tab{position:absolute;top:32px;font-size:12px;font-weight:700;font-style:italic;letter-spacing:.04em;line-height:1.15;text-transform:uppercase}
  .section-tab::before{content:"";position:absolute;top:-14px;height:26px;border-top:1px solid var(--white)}
  .page--feature .section-tab{left:46px}
  .page--feature .section-tab::before{left:-46px;width:210px;border-right:1px solid var(--white);border-top-right-radius:10px}
  .headline-disc{position:absolute;left:185px;top:200px;width:170px;height:170px;border-radius:50%;background:var(--teal);opacity:.92;
    display:flex;align-items:center;justify-content:center;text-align:center;font-size:19px;font-weight:300;font-style:italic;line-height:1.25;padding:18px}
  .divider{position:absolute;left:0;top:490px;width:550px;border-top:1px solid var(--white)}
  .callout{position:absolute;right:110px;top:540px;text-align:right;font-size:17px;font-weight:300;font-style:italic;line-height:1.55}
  .callout-bracket{position:absolute;right:88px;top:528px;width:60px;height:62px;border-top:1px solid var(--white);border-right:1px solid var(--white);border-top-right-radius:10px}
  .callout-dot{position:absolute;right:82px;top:588px;width:13px;height:13px;border:1px solid var(--white);border-radius:50%}
  .folio{position:absolute;bottom:38px;left:0;right:0;display:flex;justify-content:center;align-items:center;gap:6px;font-size:7px;letter-spacing:.12em;text-transform:uppercase}
  .folio-num{width:14px;height:14px;border-radius:50%;background:var(--white);color:var(--ink-dark);font-size:7px;font-weight:700;display:flex;align-items:center;justify-content:center}
  .folio::after{content:"";position:absolute;left:50%;top:16px;height:22px;border-left:1px solid var(--white)}

  /* Right page */
  .page--team{background:linear-gradient(200deg,var(--blue-light) 0%,var(--blue) 35%,var(--blue-deep) 100%)}
  .page--team .section-tab{right:40px;top:40px;text-align:left}
  .page--team .section-tab::before{left:-12px;width:240px;border-left:1px solid var(--white);border-top-left-radius:10px}
  .team{position:absolute;left:36px;top:110px;right:34px;display:flex;flex-direction:column;gap:24px}
  .member{display:flex;gap:18px;align-items:flex-start}
  .member-photo{flex:0 0 150px;height:104px;background:linear-gradient(180deg,#bdbdbd,var(--photo));border-radius:14px 4px 4px 4px}
  .member-body{flex:1}
  .member-name{font-size:17px;line-height:1.1;text-transform:uppercase;letter-spacing:.01em;margin-bottom:4px}
  .member-name strong{font-weight:700}
  .member-name span{font-weight:400}
  .member-bio{font-size:9.4px;font-weight:300;line-height:1.45;color:var(--soft)}
  .page--team .folio-num{color:var(--blue-deep)}
</style>
</head>
<body>
<main class="spread">
  <section class="page page--feature">
    <div class="feature-image" role="img" aria-label="Photo of hands typing on a keyboard with a glowing network globe overlay, tinted olive and lime"></div>
    <div class="section-tab">Online Asset<br>Management</div>
    <div class="headline-disc">Manage your plumbing services at the push of a button.</div>
    <div class="divider"></div>
    <div class="callout-bracket"></div>
    <div class="callout-dot"></div>
    <p class="callout">An online asset<br>management<br>system designed for<br>commercial property<br>management.</p>
    <div class="folio">Harbourline Plumbing <span class="folio-num">06</span> Capability Statement</div>
  </section>

  <section class="page page--team">
    <div class="section-tab">Meet the Team</div>
    <div class="team">
      <article class="member">
        <div class="member-photo" role="img" aria-label="Portrait photo of the managing director"></div>
        <div class="member-body">
          <h2 class="member-name"><strong>Daniel Carver</strong> <span>Managing Director</span></h2>
          <p class="member-bio">Daniel believes that quality professional relationships are built on the four key values of respect, integrity, teamwork and accountability. His aim is to provide business focused solutions to companies he works with, and gaining a thorough understanding of each organisation in order to work as a partner, rather than sub-contractor. A licensed Plumber, Gas-Fitter and registered Builder, with over 20 years' experience in commercial and construction Plumbing and maintenance, he has a hands-on approach to business, working closely with clients, consultants, authorities and other stakeholders to deliver the project from concept to completion.</p>
        </div>
      </article>
      <article class="member">
        <div class="member-photo" role="img" aria-label="Portrait photo of the second managing director"></div>
        <div class="member-body">
          <h2 class="member-name"><strong>Marco Vitale</strong> <span>Managing Director</span></h2>
          <p class="member-bio">Marco is passionate about providing quality service of the highest possible standard and leads the way in implementing industry innovations. Through collaboration with Daniel and a commitment to ensuring customer's needs are understood and met, Marco's professional approach keeps the whole team on track. Marco has over 20 years' experience in the large-scale commercial Plumbing industry. As a licensed Plumber, Gas-Fitter and registered Builder, he is an expert in all aspects of building and construction. Marco enjoys working.</p>
        </div>
      </article>
      <article class="member">
        <div class="member-photo" role="img" aria-label="Portrait photo of the construction manager"></div>
        <div class="member-body">
          <h2 class="member-name"><strong>Ben Kessler</strong> <span>Construction Manager</span></h2>
          <p class="member-bio">Ben has been involved in large scale commercial and construction Plumbing for over 10 years, working in a variety of settings all over Australia. He has been an integral part of the Harbourline Plumbing team since 2012, overseeing all construction Projects. His strong work ethic means he is highly respected on-site and ensures that every Project runs efficiently and is completed on time, to all specifications.</p>
        </div>
      </article>
      <article class="member">
        <div class="member-photo" role="img" aria-label="Portrait photo of the operations manager"></div>
        <div class="member-body">
          <h2 class="member-name"><strong>Ryan Whitford</strong> <span>Operations Manager</span></h2>
          <p class="member-bio">Ryan has over fifteen years' Project Management experience in the commercial Plumbing and construction industry. His impressive work history on large-scale infrastructure means he has a high level of technical knowledge, combined with an in-depth understanding of business management. His focus is on establishing quality relationships and maintaining effective communication with all stakeholders to ensure all of our clients have a positive experience at every stage of the Project.</p>
        </div>
      </article>
    </div>
    <div class="folio">Harbourline Plumbing <span class="folio-num">07</span> Capability Statement</div>
  </section>
</main>
</body>
</html>
```